Consulting company with focus on aviation needs

We need a new business card design for our company. The company consults with multiple players in the industry like manufacturers and airlines. It is also a supplier and an inter-company level. Given the targeted industry (aviation) it should be both kind of serious, sound, secure, classy, ​​but also a bit technical, innovative. Should not be too playful, however, "fresh", "airy", "ligth" and "suprising" are suitabe attributes. The existing logo shall be used.

Industry/Entity Type

Airlines

```html
<!DOCTYPE html>
<html lang="en">
<head>
<meta charset="utf-8">
<title>Velaro Business Card</title>
<link rel="stylesheet" href="https://fonts.googleapis.com/css2?family=Questrial&display=swap">
<style>
  :root {
    --page: #e6e4e0;
    --card-white: #ffffff;
    --card-grey: #6e7371;
    --ink-grey: #5f6462;
    --rule-grey: #9a9d9b;
    --orange: #e8922a;
    --green: #8db04a;
    --teal: #1f9a7c;
    --band-grey: #6e7371;
  }
  * { margin: 0; padding: 0; box-sizing: border-box; }
  html, body { width: 1200px; height: 900px; overflow: hidden; }
  body {
    background: var(--page);
    font-family: "Questrial", "Century Gothic", sans-serif;
    position: relative;
  }
  .card {
    position: absolute;
    left: 280px;
    width: 640px;
    height: 366px;
    border-radius: 18px;
    overflow: hidden;
    box-shadow: 0 6px 18px rgba(0,0,0,0.18);
  }
  .card-back { top: 56px; background: var(--card-grey); }
  .card-front { top: 478px; background: var(--card-white); }
  .card svg { display: block; width: 640px; height: 366px; }
</style>
</head>
<body>

<section class="card card-back" aria-label="Business card, back side">
  <svg viewBox="0 0 640 366" xmlns="http://www.w3.org/2000/svg">
    <circle class="brand-dot" cx="320" cy="128" r="34" fill="#ffffff"/>
    <text class="brand-name" x="320" y="220" text-anchor="middle" font-family="Questrial, sans-serif" font-size="50" letter-spacing="8" fill="#ffffff">VELARO</text>
    <text class="brand-tagline" x="320" y="250" text-anchor="middle" font-family="Questrial, sans-serif" font-size="14" letter-spacing="0.5" fill="#ffffff">Linking Partners - Shaping Flight</text>
  </svg>
</section>

<section class="card card-front" aria-label="Business card, front side">
  <svg viewBox="0 0 640 366" xmlns="http://www.w3.org/2000/svg" font-family="Questrial, sans-serif">
    <g class="brand">
      <circle cx="452" cy="58" r="24" fill="#1f9a7c"/>
      <text x="600" y="122" text-anchor="end" font-size="38" letter-spacing="6" fill="#5f6462">VELARO</text>
      <text x="600" y="142" text-anchor="end" font-size="11.5" fill="#e8922a">Linking Partners - Shaping Flight</text>
    </g>

    <g class="identity">
      <text x="40" y="146" font-size="28" fill="#e8922a">Mark Ellison</text>
      <text x="42" y="168" font-size="16" fill="#4a4e4c">President</text>
    </g>

    <line class="divider" x1="40" y1="182" x2="600" y2="182" stroke="#9a9d9b" stroke-width="1.5"/>

    <g class="contacts" font-size="14" fill="#4a4e4c">
      <path d="M44 202 q0 8 8 8 l2 -3 -3 -2 -2 1 q-2 -1 -3 -3 l1 -2 -2 -3 z" fill="#1f9a7c"/>
      <text x="64" y="210">555 010 4821</text>
      <rect x="45" y="218" width="8" height="13" rx="1.5" fill="none" stroke="#8db04a" stroke-width="1.6"/>
      <text x="64" y="231">555 010 7364</text>
      <rect x="43" y="242" width="13" height="9" fill="#e8922a"/>
      <path d="M43 242 l6.5 5 6.5 -5" fill="none" stroke="#ffffff" stroke-width="1"/>
      <text x="64" y="252">info@velaroconsult.net</text>
    </g>

    <g class="address" font-size="13.5" fill="#4a4e4c" text-anchor="end">
      <text x="600" y="210">Level 5, 210 Harbour Lane</text>
      <text x="600" y="229">Melbourne, VIC 3000</text>
    </g>

    <g class="footer-bands">
      <polygon points="0,350 188,350 182,360 0,360" fill="#1f9a7c"/>
      <polygon points="196,340 384,340 376,352 190,352" fill="#8db04a"/>
      <polygon points="392,328 570,328 560,342 384,342" fill="#e8922a"/>
      <polygon points="478,300 640,300 640,366 0,366 0,362 452,362" fill="#6e7371"/>
      <line x1="0" y1="363" x2="640" y2="363" stroke="#1f9a7c" stroke-width="3"/>
      <text x="612" y="326" text-anchor="end" font-size="14" fill="#ffffff">www.velaroconsult.net</text>
    </g>
  </svg>
</section>

</body>
</html>
```